Security business needs NDA formatted.

We need our NDA formatted properly and to look modern with our logo. Anybody can paste words into a document, but we need something clean, modern, DocuSign-friendly, and stylish.

```html
<!DOCTYPE html>
<html lang="en">
<head>
<meta charset="utf-8">
<title>Terravane Non-Disclosure Agreement</title>
<link rel="stylesheet" href="https://fonts.googleapis.com/css2?family=Montserrat:wght@300;400;500;600;700;800&display=swap">
<style>
:root{
  --bg:#e6e6e6;
  --paper:#ffffff;
  --paper-shade:#f1f1f1;
  --ink:#111111;
  --text:#555555;
  --muted:#8c8c8c;
  --rule:#2a2a2a;
  --edge:#cdcdcd;
}
*{box-sizing:border-box;margin:0;padding:0}
html,body{width:1200px;height:960px;overflow:hidden}
body{background:var(--bg);font-family:"Montserrat",sans-serif;color:var(--text);position:relative}

.page{position:absolute;background:var(--paper);border:1px solid var(--edge);overflow:hidden}
.page--large{width:354px;height:459px;top:121px}
.page--cover{left:245px;background:linear-gradient(170deg,var(--paper) 0%,var(--paper) 40%,var(--paper-shade) 100%)}
.page--clauses{left:607px}

.brand{position:absolute;display:flex;align-items:center;gap:6px;color:var(--ink);font-weight:600}
.brand__dot{border-radius:50%;background:var(--ink);flex:none}
.brand--cover{left:120px;top:37px;font-size:17px}
.brand--cover .brand__dot{width:28px;height:28px}

.page-footer{position:absolute;left:29px;right:40px;top:421px;display:flex;justify-content:space-between;align-items:center}
.page-footer .brand{position:static;color:var(--muted);font-size:8px;gap:4px}
.page-footer .brand__dot{width:13px;height:13px;background:var(--muted)}
.page-footer__num{font-size:6.5px;color:var(--muted)}

.doc-title{position:absolute;left:0;right:0;top:104px;text-align:center;font-weight:800;font-size:12.5px;color:var(--ink);letter-spacing:.1px}
.doc-title::before{content:"";display:inline-block;border-left:3.5px solid var(--ink);border-top:3px solid transparent;border-bottom:3px solid transparent;margin-right:5px;vertical-align:1.5px}

.parties{position:absolute;left:0;right:0;top:147px;text-align:center;font-size:7.2px;line-height:11px;color:var(--text)}
.parties strong{color:var(--ink);font-weight:700}
.parties .gap{height:5px}

.background{position:absolute;left:32px;right:30px;top:303px;font-size:5.9px;line-height:9.3px;font-weight:300;color:#444}
.background h3{font-size:7px;font-weight:800;color:var(--ink);margin-bottom:7px}
.background .recital{display:flex;margin-bottom:7px}
.background .recital b{width:19px;flex:none;color:var(--ink);font-weight:800;font-size:7px}
.background .consideration strong{color:var(--ink);font-weight:800;font-size:6.8px}

.section-head{position:absolute;left:30px;right:30px;top:23px;padding:0 0 4px 22px;border-bottom:1px solid var(--rule);font-weight:700;font-size:7px;color:var(--ink)}
.clause{position:absolute;left:32px;right:32px;font-size:5.9px;line-height:9.2px;font-weight:300;color:#444;display:flex}
.clause__n{width:19px;flex:none;font-weight:700;color:var(--ink)}
.clause--sub{left:51px}

.page--mini{width:136px;height:176px;top:688px}
.mini-body{position:absolute;left:14px;right:14px;top:7px}
.mini-body h4{font-size:2.8px;font-weight:700;color:var(--ink);border-bottom:.5px solid var(--rule);padding:0 0 1.5px 6px;margin:2px 0 3px}
.mini-body p{position:relative;font-size:2.4px;line-height:3.3px;padding-left:8px;margin-bottom:3px;color:#555}
.mini-body p b{position:absolute;left:1px;color:var(--ink)}
.mini-footer{position:absolute;left:11px;right:14px;top:162px;display:flex;justify-content:space-between;align-items:center}
.mini-footer .brand{position:static;color:var(--muted);font-size:3px;gap:2px}
.mini-footer .brand__dot{width:5px;height:5px;background:var(--muted)}
.mini-footer span{font-size:2.2px;color:var(--muted)}

.witness{position:absolute;left:12px;right:12px;top:86px;font-size:2.4px;line-height:3.3px;color:#555}
.witness strong{color:var(--ink)}
.signatory{position:absolute;left:75px;width:46px;font-size:2.3px;line-height:3.3px}
.signatory strong{display:block;color:var(--ink);margin-bottom:3px}
.signatory .line{display:flex;gap:1px}
.signatory .line i{flex:1;border-bottom:.4px solid #888;height:2.6px}
</style>
</head>
<body>

<section class="page page--large page--cover">
  <div class="brand brand--cover"><span class="brand__dot"></span>Terravane</div>
  <h1 class="doc-title">NON-DISCLOSURE&nbsp; AGREEMENT</h1>
  <div class="parties">
    <strong>BETWEEN:</strong>
    <div class="gap"></div>
    <div>ACME of 58 Orchard Row, CA, 90000, USA</div>
    <strong>(the «Company»)</strong>
    <div>of the first part</div>
    <div class="gap"></div>
    <strong>- AND -</strong>
    <div class="gap"></div>
    <div>COMPANY NAME of COMPANY ADDRESS</div>
    <strong>(the «Evaluator»)</strong>
    <div>of the second part</div>
  </div>
  <div class="background">
    <h3>BACKGROUND:</h3>
    <div class="recital"><b>A.</b><span>ACME has proprietary information and know-how relating to certain investigation tools and tactics (the "Company").</span></div>
    <div class="recital"><b>B.</b><span>In connection with the Evaluator evaluating the Invention for possible patent, development, and marketing (the "Permitted Purpose"), the Evaluator has requested certain confidential information (the "Confidential Information") regarding the Company.</span></div>
    <p class="consideration"><strong>IN CONSIDERATION OF</strong> and as a condition of the Company providing the Confidential Information to the Evaluator in addition to other valuable consideration, the receipt and sufficiency of which consideration is hereby acknowledged, the parties to this Agreement agree as follows:</p>
  </div>
  <footer class="page-footer"><div class="brand"><span class="brand__dot"></span>Terravane</div><span class="page-footer__num">Page 1 of 9</span></footer>
</section>

<section class="page page--large page--clauses">
  <h2 class="section-head">Confidential Information</h2>
  <div class="clause" style="top:50px"><span class="clause__n">1.</span><span>All written and oral information and materials disclosed or provided by the Company to the Evaluator under this Agreement constitute Confidential Information regardless of whether such information was provided before or after the date of this Agreement or how it was provided to the Evaluator.</span></div>
  <div class="clause" style="top:95px"><span class="clause__n">2.</span><span>'Confidential Information' means all data and information relating to the invention as well as data and information relating to the Company, including but not limited to, the following:</span></div>
  <div class="clause clause--sub" style="top:121px"><span class="clause__n">a.</span><span>'Business Operations' which includes internal personnel and financial information of the Company, vendor names and other vendor information (including vendor characteristics, services and agreements), purchasing and internal cost information, internal services and operational manuals, external business contacts including those stored on social media accounts or other similar platforms or databases operated by the Company, and the manner and methods of conducting the Company's business;</span></div>
  <div class="clause clause--sub" style="top:184px"><span class="clause__n">b.</span><span>'Customer Information' which includes names of customers of the Company, their representatives, all customer contact information, contracts and their contents and parties, customer services, data provided by customers and the type, quantity and specifications of products and services purchased, leased, licensed or received by customers of the Company;</span></div>
  <div class="clause clause--sub" style="top:237px"><span class="clause__n">c.</span><span>'Intellectual Property' which includes information relating to the Company's proprietary rights prior to any public disclosure of such information, including but not limited to the nature of the proprietary rights, production data, technical and engineering data, technical concepts, test data and test results, simulation results, the status and details of research and development of products and services, and information regarding acquiring, protecting, enforcing and licensing proprietary rights (including patents, copyrights and trade secrets);</span></div>
  <div class="clause clause--sub" style="top:308px"><span class="clause__n">d.</span><span>'Service Information' which includes all data and information relating to the services provided by the Company, including but not limited to, plans, schedules, manpower, inspection, and training information;</span></div>
  <div class="clause clause--sub" style="top:343px"><span class="clause__n">e.</span><span>'Product Information' which includes all specifications for products of the Company as well as work product resulting from or related to work or projects of the Company, of any type or form in any stage of actual or anticipated research and development;</span></div>
  <div class="clause clause--sub" style="top:373px"><span class="clause__n">f.</span><span>'Production Processes' which includes processes used in the creation, production and manufacturing of the work product of the Company, including but not limited to, formulas, patterns, molds, models, methods, techniques, specifications, processes, procedures, equipment, devices, programs, and designs;</span></div>
  <footer class="page-footer"><div class="brand"><span class="brand__dot"></span>Terravane</div><span class="page-footer__num">Page 2 of 9</span></footer>
</section>

<section class="page page--mini" style="left:111px">
  <div class="mini-body" style="top:10px">
    <p><b>g.</b>'Accounting Information' which includes financial statements, annual reports, balance sheets and tax records of the Company;</p>
    <p><b>h.</b>'Marketing and Development Information' which includes marketing plans, pricing, forecasts and sales strategies of the Company;</p>
    <p><b>i.</b>'Computer Technology' which includes scientific and technical information, designs, methods and know-how of the Company;</p>
    <p><b>j.</b>'Proprietary Computer Code' which includes source code, object code, programs and related documentation of the Company;</p>
    <p><b>3.</b>Confidential Information will not include information that is generally known, already held, or independently created by the Evaluator.</p>
  </div>
  <footer class="mini-footer"><div class="brand"><span class="brand__dot"></span>Terravane</div><span>Page 3 of 9</span></footer>
</section>

<section class="page page--mini" style="left:251px">
  <div class="mini-body">
    <h4>Obligations of Non-Disclosure</h4>
    <p><b>4.</b>Except as otherwise provided in this Agreement, the Evaluator must not disclose the Confidential Information.</p>
    <p><b>5.</b>Confidential Information will remain the exclusive property of the Company and be used only for the Permitted Purpose.</p>
    <p><b>6.</b>These obligations will survive the expiry or termination of this Agreement and last indefinitely.</p>
    <p><b>7.</b>The Evaluator may disclose Confidential Information only to personnel who need to know it, or where required by law.</p>
    <p><b>8.</b>The Evaluator will keep all Confidential Information at its usual place of business, separate from other records.</p>
  </div>
  <footer class="mini-footer"><div class="brand"><span class="brand__dot"></span>Terravane</div><span>Page 4 of 9</span></footer>
</section>

<section class="page page--mini" style="left:394px">
  <div class="mini-body">
    <h4>Non-Solicitation</h4>
    <p><b>9.</b>The Evaluator will not solicit any person employed by the Company for two years.</p>
    <h4>Non-Competition</h4>
    <p><b>10.</b>The Evaluator will not compete with the Company in the market for the Invention.</p>
    <h4>Ownership and Title</h4>
    <p><b>11.</b>Nothing in this Agreement grants the Evaluator any right or licence to the Company's property.</p>
    <h4>Remedies</h4>
    <p><b>12.</b>Any breach may cause irreparable harm, and the Company may seek an injunction in addition to other remedies available at law.</p>
    <h4>Return of Confidential Information</h4>
    <p><b>13.</b>On request, the Evaluator will promptly return all Confidential Information to the Company.</p>
  </div>
  <footer class="mini-footer"><div class="brand"><span class="brand__dot"></span>Terravane</div><span>Page 5 of 9</span></footer>
</section>

<section class="page page--mini" style="left:533px">
  <div class="mini-body">
    <p><b>a.</b>return all Confidential Information to the Company; b. certify in writing that it has been returned.</p>
    <h4>Notices</h4>
    <p><b>14.</b>If legally required to disclose information, the Evaluator will give the Company prompt written notice.</p>
    <p><b>15.</b>The Evaluator will report any unauthorised disclosure immediately.</p>
    <p><b>16.</b>Notices are delivered by hand, post or email to the addresses below.</p>
    <p><b>17.</b>a. ACME, 58 Orchard Row, CA<br>b. COMPANY NAME, COMPANY ADDRESS</p>
    <h4>Representations</h4>
    <p><b>18.</b>The Company makes no representation as to the accuracy or completeness of the Confidential Information.</p>
  </div>
  <footer class="mini-footer"><div class="brand"><span class="brand__dot"></span>Terravane</div><span>Page 6 of 9</span></footer>
</section>

<section class="page page--mini" style="left:676px">
  <div class="mini-body">
    <h4>Further Agreements</h4>
    <p><b>19.</b>If the Invention is worth developing, the parties may negotiate a further agreement.</p>
    <h4>Termination</h4>
    <p><b>20.</b>Either party may end this Agreement by written notice to the other party.</p>
    <h4>Assignment</h4>
    <p><b>21.</b>This Agreement may not be assigned without prior written consent.</p>
    <h4>Amendments</h4>
    <p><b>22.</b>This Agreement may only be amended in writing by both parties.</p>
    <h4>Governing Law</h4>
    <p><b>23.</b>This Agreement is governed by the laws of the State.</p>
    <h4>General Provisions</h4>
    <p><b>24.</b>Time is of the essence. 25. This Agreement may be signed in counterpart.</p>
  </div>
  <footer class="mini-footer"><div class="brand"><span class="brand__dot"></span>Terravane</div><span>Page 7 of 9</span></footer>
</section>

<section class="page page--mini" style="left:815px">
  <div class="mini-body" style="top:9px">
    <p><b>26.</b>Clauses are read independently; an invalid clause does not affect the rest.</p>
    <p><b>27.</b>The Evaluator is liable for all costs incurred by the Company in enforcing this Agreement.</p>
    <p><b>28.</b>The parties agree this Agreement is reasonable and fair, and a court may narrow any term to make it enforceable.</p>
    <p><b>29.</b>No delay in exercising any right will operate as a waiver of that right.</p>
    <p><b>30.</b>This Agreement binds the parties and their successors and assigns.</p>
    <p><b>31.</b>This is the entire agreement between the parties.</p>
  </div>
  <footer class="mini-footer"><div class="brand"><span class="brand__dot"></span>Terravane</div><span>Page 8 of 9</span></footer>
</section>

<section class="page page--mini" style="left:957px">
  <p class="witness"><strong>IN WITNESS WHEREOF</strong> ACME and COMPANY NAME have duly affixed their signatures under hand and seal on this ________ day of ____________.</p>
  <div class="signatory" style="top:101px"><strong>ACME</strong><div class="line">Per:<i></i></div><div>(Seal)</div></div>
  <div class="signatory" style="top:121px"><strong>COMPANY NAME</strong><div class="line">Per:<i></i></div><div>(Seal)</div></div>
  <footer class="mini-footer"><div class="brand"><span class="brand__dot"></span>Terravane</div><span>Page 9 of 9</span></footer>
</section>

</body>
</html>
```